Local Horticulturalist needs Business card design

Meridel Horticulture would like to update our existing business card and utilize our new logo (design attached)....we specialize in getting the best out of our customers yard with professional maintenance programs, expert pruning and hedging and garden restorations.
Utilizing colors from attached logo I would like a design that implies professionalism and if possible our businesses love of restoration through plants.
I also sometimes write down for my customers a start date and price on the back of my current card
Target Market(s)
Home owners
Contractors
Industry/Entity Type
Gardener
Contact Information for Business Card
Gareth Volkstrom | Horticulturalist
ph: 0438275946
meridelhort@fernmail.example
www.meridelhorticulture.example.au
Requirements
Must have
- crucial information easy to read
- incorporate current logo
- Horticulturalist listed preferably near name
Nice to have
- currently I write a job start date and price on the back of my current card so something that integrates this would be beneficial
Should not have
- be pretty or flowerey
- be too white or basic

```html
<!DOCTYPE html>
<html lang="en">
<head>
<meta charset="utf-8">
<title>Meridel Horticulture — Business Card</title>
<link rel="stylesheet" href="https://fonts.googleapis.com/css2?family=Source+Sans+3:wght@400;600;700&family=PT+Sans+Narrow:wght@400;700&display=swap">
<style>
  :root {
    --leaf-green: #8bc53f;
    --soil-brown: #7b6a4f;
    --band-green: #819c57;
    --card-white: #ffffff;
    --card-edge: #111111;
    --page: #ffffff;
  }
  * { box-sizing: border-box; margin: 0; padding: 0; }
  html, body {
    width: 927px; height: 1200px; overflow: hidden; background: var(--page);
  }
  .sheet { position: relative; width: 927px; height: 1200px; }
  .card {
    position: absolute; left: 116px; width: 695px; height: 397px;
    background: var(--card-white); border: 2px solid var(--card-edge); overflow: hidden;
  }
  .card--front { top: 105px; }
  .card--back { top: 696px; }

  .brand-dot {
    position: absolute; left: 41px; top: 40px; width: 90px; height: 90px;
    border-radius: 50%; background: var(--leaf-green);
  }
  .brand-name {
    position: absolute; left: 142px; top: 52px;
    font-family: "Source Sans 3", sans-serif; font-weight: 700; font-size: 46px;
    line-height: 1; color: var(--soil-brown); white-space: nowrap;
  }
  .brand-tagline {
    position: absolute; left: 150px; top: 108px;
    font-family: "Source Sans 3", sans-serif; font-weight: 600; font-size: 19px;
    letter-spacing: 1.2px; color: var(--soil-brown); white-space: nowrap;
  }
  .person { position: absolute; left: 37px; top: 172px; color: var(--soil-brown);
    font-family: "Source Sans 3", sans-serif; font-size: 28px; line-height: 36px; }
  .person__name { font-weight: 600; }
  .person__role { font-weight: 400; }

  .contacts { position: absolute; left: 37px; top: 274px; list-style: none;
    font-family: "PT Sans Narrow", sans-serif; font-weight: 700; font-size: 24px;
    line-height: 30px; color: var(--soil-brown); }
  .contacts__label { color: var(--band-green); }

  .mark-area {
    position: absolute; left: 54px; top: 57px; width: 286px; height: 286px;
    border-radius: 50%; background: var(--leaf-green);
  }
  .job-band { position: absolute; left: 377px; top: 0; width: 318px; height: 397px;
    background: var(--band-green); }
  .note-box {
    position: absolute; left: 51px; width: 216px; height: 108px; background: var(--card-white);
    font-family: "PT Sans Narrow", sans-serif; font-weight: 700; font-size: 26px;
    color: var(--soil-brown); text-align: center; padding-top: 6px;
  }
  .note-box--date { top: 66px; }
  .note-box--price { top: 216px; }
</style>
</head>
<body>
<main class="sheet">
  <section class="card card--front" aria-label="Card front">
    <div class="brand-dot" aria-hidden="true"></div>
    <div class="brand-name">Meridel Horticulture</div>
    <div class="brand-tagline">Garden Restorations &amp; Maintenance</div>

    <div class="person">
      <div class="person__name">Gareth Volkstrom</div>
      <div class="person__role">Horticulturist</div>
    </div>

    <ul class="contacts">
      <li><span class="contacts__label">PHONE</span> | 043·827·5946</li>
      <li><span class="contacts__label">EMAIL</span> | meridelhort@fernmail.example</li>
      <li><span class="contacts__label">WEB</span> | www.meridelhorticulture.example.au</li>
    </ul>
  </section>

  <section class="card card--back" aria-label="Card back">
    <div class="mark-area" role="img" aria-label="Large brand mark area"></div>
    <div class="job-band">
      <div class="note-box note-box--date">JOB START DATE</div>
      <div class="note-box note-box--price">PRICE</div>
    </div>
  </section>
</main>
</body>
</html>
```